Business Card for By Karel Voss

Looking to have a business card designed for my lifestyle and fitness company. My company offers personal training, online programming and nutrition advice based out of London, United Kingdom.

I'd like to see modern, sleek designs, focusing on black, matte black or matte grey. Design doesn't need to be overly descriptive as this will also be used as a personal business card. I've included my logo.

Please note that my company is no longer called "Fitness by Karel Voss" but instead "By Karel Voss", this is because of my other ventures. Therefore please don't use the "fitness by karel voss" text.

information about my company can be found at www.bykarelvoss.com

Company is also based out of London (United Kingdom) & Sydney (Australia) this could be reflected on the card.

Industry/Entity Type

Business

Contact Information for Business Card

Karel Voss
+44 7382 615027
karel@bykarelvoss.com
www.bykarelvoss.com

Font styles to use
Sans Serif

Requirements
Must have
• All contact details and inclusion of my logo.

```html
<!DOCTYPE html>
<html lang="en">
<head>
<meta charset="utf-8">
<title>By Karel Voss — Business Card</title>
<link rel="stylesheet" href="https://fonts.googleapis.com/css2?family=Roboto:wght@400;500;700;900&family=Roboto+Condensed:wght@500&display=swap">
<style>
  :root {
    --backdrop: #2a2a2a;
    --card-light: #f1f1f1;
    --card-dark: #1e1e1e;
    --ink: #1c1c1c;
    --ink-soft: #3a3a3a;
    --paper: #ffffff;
    --edge-dark: #252525;
    --edge-grey: #bdbdbd;
  }
  * { margin: 0; padding: 0; box-sizing: border-box; }
  html, body {
    width: 1200px; height: 960px; overflow: hidden;
    background: var(--backdrop);
    font-family: "Roboto", Arial, sans-serif;
  }
  .canvas { position: relative; width: 1200px; height: 960px; }

  .card { position: absolute; width: 600px; box-shadow: 0 4px 14px rgba(0,0,0,.45); }

  /* Front */
  .card-front { left: 314px; top: 113px; height: 342px; background: var(--card-light); }
  .card-front .edge {
    position: absolute; left: 0; bottom: 0; width: 100%; height: 10px;
    background: linear-gradient(100deg, var(--edge-dark) 0 65%, var(--edge-grey) 65.2% 100%);
  }
  .brand-front {
    position: absolute; right: 42px; top: 140px;
    display: flex; align-items: center; gap: 10px;
    font-weight: 900; font-size: 24px; letter-spacing: .5px;
    text-transform: uppercase; color: var(--ink);
  }
  .brand-mark { width: 14px; height: 14px; border-radius: 50%; background: var(--ink); }
  .holder-name {
    position: absolute; left: 43px; top: 201px;
    font-family: "Roboto Condensed", Arial, sans-serif;
    font-weight: 500; font-size: 22px; color: var(--ink);
  }
  .rule { position: absolute; left: 43px; top: 233px; width: 515px; height: 1px; background: var(--ink); }
  .contact-list { position: absolute; left: 43px; top: 249px; list-style: none; }
  .contact-list li {
    display: flex; align-items: center; gap: 8px;
    height: 19px; font-size: 14px; color: var(--ink-soft);
  }
  .contact-list svg { width: 13px; height: 13px; fill: var(--ink); }

  /* Back */
  .card-back { left: 312px; top: 473px; height: 342px; background: var(--card-dark); }
  .brand-back {
    position: absolute; left: 0; right: 0; top: 138px;
    display: flex; justify-content: center; align-items: center; gap: 12px;
    font-weight: 900; font-size: 30px; letter-spacing: .5px;
    text-transform: uppercase; color: var(--paper);
  }
  .brand-back .brand-mark { background: var(--paper); width: 16px; height: 16px; }
  .back-web {
    position: absolute; left: 0; right: 0; top: 288px; text-align: center;
    font-size: 15px; letter-spacing: 3.2px; color: var(--paper);
  }
</style>
</head>
<body>
<main class="canvas">
  <section class="card card-front">
    <div class="brand-front"><span class="brand-mark"></span>By Karel Voss</div>
    <h1 class="holder-name">KAREL VOSS</h1>
    <div class="rule"></div>
    <ul class="contact-list">
      <li>
        <svg viewBox="0 0 16 16" aria-hidden="true"><path d="M4 0h8a1 1 0 0 1 1 1v14a1 1 0 0 1-1 1H4a1 1 0 0 1-1-1V1a1 1 0 0 1 1-1zm1 2v10h6V2H5zm3 11a1 1 0 1 0 0 2 1 1 0 0 0 0-2z"/></svg>
        +44 7382 615027
      </li>
      <li>
        <svg viewBox="0 0 16 16" aria-hidden="true"><path d="M1 3h14v10H1V3zm1.5 1L8 8.5 13.5 4h-11z"/></svg>
        karel@bykarelvoss.com
      </li>
      <li>
        <svg viewBox="0 0 16 16" aria-hidden="true"><path d="M8 0a8 8 0 1 0 0 16A8 8 0 0 0 8 0zm-1 3l3 1-1 3 3 2-1 4-3-3-3 1 1-4-3-1 2-3h2z"/></svg>
        www.bykarelvoss.com
      </li>
    </ul>
    <div class="edge"></div>
  </section>

  <section class="card card-back">
    <div class="brand-back"><span class="brand-mark"></span>By Karel Voss</div>
    <p class="back-web">www.bykarelvoss.com</p>
  </section>
</main>
</body>
</html>
```